Create a professional, eye-catching business card design that reflects the values and services of Brookfern Veterinary Hospital. we provide veterinary services and the business card should be a memorable representation of the clinic and align with its branding and mission. our tag line is "Every Step Together, Gentle Care"
Use clean, modern typography. Prioritize readability and professionalism. We would like to see designs that use the color blue, as in the logo example. the final design should communicate professionalism and care, with attention to detail.

```html
<!DOCTYPE html>
<html lang="en">
<head>
<meta charset="utf-8">
<title>Brookfern Veterinary Hospital – Business Card</title>
<link rel="stylesheet" href="https://fonts.googleapis.com/css2?family=Roboto:wght@400;500;700&family=Great+Vibes&display=swap">
<style>
  :root {
    --backdrop: #1c1c1e;
    --card-navy: #1e2f6b;
    --card-navy-deep: #18275a;
    --ink-white: #ffffff;
    --ink-soft: rgba(255,255,255,0.85);
    --art-light: #3e55a6;
    --art-dark: #233777;
  }
  * { box-sizing: border-box; margin: 0; padding: 0; }
  html, body { width: 1200px; height: 801px; overflow: hidden; }
  body {
    background: var(--backdrop);
    font-family: "Roboto", Arial, sans-serif;
    display: flex;
    align-items: center;
    justify-content: center;
    gap: 40px;
  }
  .card {
    position: relative;
    width: 560px;
    height: 320px;
    border-radius: 22px;
    background: linear-gradient(160deg, var(--card-navy) 0%, var(--card-navy-deep) 100%);
    overflow: hidden;
    color: var(--ink-white);
  }
  /* Front */
  .brand {
    position: absolute;
    left: 40px;
    top: 110px;
    width: 230px;
    display: flex;
    align-items: center;
    gap: 14px;
  }
  .brand-dot {
    flex: none;
    width: 44px;
    height: 44px;
    border-radius: 50%;
    border: 2px solid var(--ink-white);
  }
  .brand-name {
    font-weight: 700;
    font-size: 24px;
    line-height: 1.1;
    text-transform: uppercase;
    letter-spacing: 0.5px;
  }
  .divider {
    position: absolute;
    left: 290px;
    top: 60px;
    width: 1px;
    height: 200px;
    background: var(--ink-soft);
  }
  .contact {
    position: absolute;
    left: 312px;
    top: 62px;
    font-size: 14px;
    line-height: 1.35;
  }
  .contact .person-name { font-weight: 700; font-size: 18px; text-transform: uppercase; letter-spacing: 0.5px; }
  .contact .person-role { font-size: 15px; margin-bottom: 14px; }
  .contact .address { margin-bottom: 14px; }
  .contact-row { display: flex; align-items: center; gap: 8px; }
  .contact-row svg { width: 13px; height: 13px; flex: none; }
  /* Back */
  .back-art {
    position: absolute;
    right: 24px;
    top: 30px;
    width: 250px;
    height: 250px;
    border-radius: 50%;
    background: radial-gradient(circle at 60% 65%, var(--art-dark) 0%, var(--art-light) 75%, var(--card-navy) 100%);
    opacity: 0.55;
  }
  .tagline {
    position: absolute;
    left: 36px;
    bottom: 40px;
    width: 240px;
  }
  .tagline-lead { font-size: 20px; font-weight: 400; white-space: nowrap; }
  .tagline-script {
    font-family: "Great Vibes", cursive;
    font-size: 40px;
    line-height: 1.1;
    margin-left: 40px;
    margin-top: 2px;
    white-space: nowrap;
  }
</style>
</head>
<body>
  <section class="card card-front">
    <div class="brand">
      <span class="brand-dot"></span>
      <span class="brand-name">Brookfern Veterinary Hospital</span>
    </div>
    <div class="divider"></div>
    <div class="contact">
      <div class="person-name">Daniel Hartley</div>
      <div class="person-role">Managing Director</div>
      <div class="address">Your Address, City<br>State, Zip 0000</div>
      <div class="contact-row">
        <svg viewBox="0 0 16 16" aria-hidden="true"><path fill="#fff" d="M3.5 1.5l2.5 0 1 3.5-1.8 1.2a8 8 0 0 0 4.6 4.6L11 9l3.5 1v2.5c0 1-1 2-2 2A11 11 0 0 1 1.5 3.5c0-1 1-2 2-2z"/></svg>
        <span>044-555 010 200</span>
      </div>
      <div class="contact-row">
        <svg viewBox="0 0 16 16" aria-hidden="true"><rect x="1" y="3" width="14" height="10" rx="1.5" fill="#fff"/><path d="M1.5 4l6.5 5 6.5-5" stroke="#1e2f6b" stroke-width="1.4" fill="none"/></svg>
        <span>hello@brookfernvet.com</span>
      </div>
      <div class="contact-row">
        <svg viewBox="0 0 16 16" aria-hidden="true"><circle cx="8" cy="8" r="7" fill="#fff"/><path d="M1 8h14M8 1c-3 3.5-3 10.5 0 14M8 1c3 3.5 3 10.5 0 14" stroke="#1e2f6b" stroke-width="1.1" fill="none"/></svg>
        <span>www.brookfernvet.com</span>
      </div>
    </div>
  </section>

  <section class="card card-back">
    <div class="back-art" role="img" aria-label="Embossed tone-on-tone illustration of a dog and cat sitting beneath a leafy branch inside a circle"></div>
    <div class="tagline">
      <div class="tagline-lead">Every Step Together</div>
      <div class="tagline-script">Gentle Care</div>
    </div>
  </section>
</body>
</html>
```